Website for Private Psychologist

DO NOT CONTACT ME PRIVATELY

I am a Psychologist offering psychotherapy for individuals and couples, and clinical consultation and training and education for mental and medical health professionals and agencies.

I need a redesign of my website

5 Pages (content is attached for each page)
Home
Jungian Psychotherapy
Clinical Consultation & Professional Development
Curriculum Vitae & Publications
Practice Policies and Forms

Designs can be based on these style websites
https://lqmindcare.info; https://pdtarn.org/; https://dorabellcroftcounselling.com/

Design Concepts
Minimalist Layout: Clean and uncluttered layout with generous white space, allowing the content and visuals to stand out'

Keep a linear, uncluttered, professional design.

Please use only royalty free images and google fonts. Please provide links to any stock images used to verify license.

Target Market(s)

private individual or couples seeking psychotherapy

Industry/Entity Type

Psychotherapy

Number of Pages Required

5+ page

Requirements
Should not have
• No search feature

```html
<!DOCTYPE html>
<html lang="en">
<head>
<meta charset="utf-8">
<title>Halvorsen — Psychotherapy</title>
<link href="https://fonts.googleapis.com/css2?family=Open+Sans:wght@400;500;600;700&display=swap" rel="stylesheet">
<style>
:root{
  --navy:#1f3c6e;
  --navy-deep:#0e2a47;
  --navy-card:#1d3c5e;
  --footer:#1e3457;
  --topbar:#1b1f36;
  --cyan:#1aa6c9;
  --cyan-light:#4cc6e6;
  --ink:#222;
  --muted:#777;
  --light:#f4f4f4;
  --white:#fff;
}
*{box-sizing:border-box;margin:0;padding:0}
html,body{width:1200px;height:4731px;overflow:hidden}
body{font-family:"Open Sans",sans-serif;color:var(--ink);background:var(--white)}
.page{position:relative;width:1200px;height:4731px;overflow:hidden}
.abs{position:absolute}
svg{display:block}

/* top bar */
.topbar{top:0;left:0;width:1200px;height:44px;background:var(--topbar);color:#cfd3e0;font-size:14px}
.topbar .item{position:absolute;top:13px;display:flex;align-items:center;gap:8px}
.topbar .links{position:absolute;right:130px;top:13px;display:flex;gap:16px}
.topbar .links span+span{border-left:1px solid #555;padding-left:16px}
.topbar .social{position:absolute;right:40px;top:16px;display:flex;gap:12px}
.topbar .social i{width:11px;height:11px;border-radius:50%;background:#9aa0b4;display:block}

/* header */
.header{top:44px;left:0;width:1200px;height:110px;background:var(--white)}
.logo{position:absolute;left:92px;top:34px;font-size:32px;font-weight:700;color:#2a2a2a}
.hinfo{position:absolute;top:30px;display:flex;gap:16px;align-items:center}
.hinfo b{display:block;font-weight:500;font-size:15px;color:#222}
.hinfo small{font-size:13px;color:#666}
.btn-estimate{position:absolute;left:957px;top:30px;width:180px;height:48px;background:var(--navy);color:#fff;font-size:14px;font-weight:600;display:flex;align-items:center;justify-content:center;gap:10px;border-radius:3px}

/* nav */
.nav{top:154px;left:78px;width:986px;height:68px;background:#fff;display:flex;align-items:center;padding-left:86px;gap:50px;font-size:14px;color:#555;z-index:2}
.nav .active{color:var(--navy);font-weight:600}
.nav-phone{top:154px;left:1064px;width:73px;height:68px;background:var(--navy);display:flex;align-items:center;justify-content:center;z-index:2}

/* hero */
.hero{top:154px;left:0;width:1200px;height:686px;background:linear-gradient(90deg,#2e3135 0%,#4a4c50 45%,#6a6a6c 100%)}
.hero-tag{position:absolute;left:100px;top:246px;width:266px;height:42px;background:var(--navy);border-left:4px solid var(--cyan-light);color:#fff;font-size:20px;font-weight:600;padding:6px 18px}
.hero h1{position:absolute;left:98px;top:282px;font-size:92px;font-weight:700;color:#fff;letter-spacing:1px}
.hero p{position:absolute;left:100px;top:406px;width:480px;font-size:16px;line-height:26px;color:#eee}
.btn-cyan{background:var(--cyan-light);color:#fff;font-size:15px;font-weight:600;display:flex;align-items:center;justify-content:center;gap:12px}
.hero .btn-cyan{position:absolute;left:100px;top:486px;width:176px;height:52px}

/* about intro */
.ph{position:absolute;border-radius:4px}
.eyebrow{font-size:12px;color:var(--cyan);text-transform:uppercase;text-decoration:underline;text-underline-offset:4px}
.h2{font-size:40px;font-weight:600;color:var(--navy);line-height:52px}
.body-s{font-size:12.5px;line-height:22px;color:#888}
.btn-sq{position:absolute;height:44px;background:var(--cyan);color:#fff;font-size:15px;font-weight:600;display:flex;align-items:center;justify-content:center;gap:14px}

/* conditions */
.conditions{top:1452px;left:0;width:1200px;height:649px;background:var(--light)}
.cond-card{position:absolute;top:209px;width:317px;height:353px;border-radius:4px;overflow:hidden}
.cond-card .title{position:absolute;left:28px;top:230px;font-size:24px;font-weight:600;color:#fff}
.cond-card .dot{position:absolute;left:20px;top:232px;width:16px;height:16px;border-radius:50%;background:var(--cyan-light)}
.cond-card .arrow{position:absolute;left:28px;top:282px;width:48px;height:48px;border-radius:50%;background:rgba(255,255,255,.25);display:flex;align-items:center;justify-content:center}

/* leading expert */
.expert-band{top:2101px;left:0;width:1200px;height:386px;background:linear-gradient(90deg,#2b4d7e,#1f3c6e 55%,#2c4a78)}
.expert-card{position:absolute;top:2213px;width:233px;height:360px;background:#fff;box-shadow:0 4px 18px rgba(0,0,0,.08);text-align:center;padding-top:50px}
.expert-card h3{font-size:19px;font-weight:600;color:#1b2b44;margin:16px 0 12px}
.expert-card p{font-size:14px;line-height:25px;color:var(--navy);padding:0 28px}
.expert-card .more{margin-top:30px;font-size:14px;font-weight:600;color:var(--navy);display:flex;justify-content:center;align-items:center;gap:8px}

/* about person */
.aboutme{top:2573px;left:0;width:1200px;height:656px;background:var(--light)}
.cred h4{font-size:19px;font-weight:500;color:#1b2b44;line-height:25px}
.cred small{font-size:12.5px;color:#666;line-height:20px;display:block;margin-top:6px}
.icircle{position:absolute;width:76px;height:76px;border-radius:50%;background:#fff;box-shadow:0 2px 10px rgba(0,0,0,.06);display:flex;align-items:center;justify-content:center}

/* testimonials */
.testimonials{top:3229px;left:0;width:1200px;height:539px;background:var(--navy-deep)}
.tcard{position:absolute;top:214px;width:322px;height:217px;background:var(--navy-card);border-radius:3px;padding:58px 30px 0 32px}
.tcard p{font-size:13px;line-height:23px;color:#e6ecf3}
.tcard .quote{position:absolute;left:145px;top:6px}
.tcard .who{display:flex;align-items:center;gap:16px;margin-top:18px}
.tcard .avatar{width:48px;height:48px;border-radius:50%;background:linear-gradient(135deg,#c9b7a5,#7d6a5c)}
.tcard .who b{display:block;color:#fff;font-weight:500;font-size:16px}
.tcard .who small{color:#8ea3bb;font-size:15px}

/* contact */
.contact-item{position:absolute;left:108px;display:flex;gap:30px;align-items:flex-start}
.contact-item b{display:block;font-size:13px;font-weight:700;color:#222}
.contact-item small{font-size:13px;color:#888}
.form-panel{top:3810px;left:596px;width:496px;height:635px;background:#fff;border-top:4px solid #a8b4c8;z-index:2;padding:52px 36px 0 38px}
.form-panel h3{font-size:24px;font-weight:600;color:#1b2b44;margin-bottom:32px}
.form-panel label{display:block;font-size:13px;font-weight:600;color:#222;margin-bottom:8px}
.field{height:42px;border:1.5px solid #cfcfcf;border-radius:21px;font-size:13px;color:#999;padding:11px 24px}
.row2{display:flex;gap:14px}
.row2>div{width:200px}
.area{height:124px;border:1.5px solid #cfcfcf;border-radius:3px;font-size:13px;color:#999;padding:16px 24px}

/* footer */
.footer{top:4356px;left:0;width:1200px;height:375px;background:var(--footer);color:#fff}
.footer .flogo{position:absolute;left:216px;top:158px;font-size:34px;font-weight:700}
.finfo{position:absolute;top:148px;display:flex;gap:12px;align-items:center;font-size:13px;line-height:20px}
.fnav{position:absolute;left:258px;top:234px;width:706px;height:60px;border-top:1px solid #4a5f80;border-bottom:1px solid #4a5f80;display:flex;justify-content:space-around;align-items:center;font-size:14px}
.copy{position:absolute;left:146px;top:334px;font-size:12px;color:#c5cedc}
.fsocial{position:absolute;left:932px;top:328px;display:flex;gap:6px}
.fsocial i{width:26px;height:26px;border:1px solid #c5cedc;display:block}
</style>
</head>
<body>
<div class="page">

  <!-- top bar -->
  <div class="abs topbar">
    <div class="item" style="left:76px">
      <svg width="15" height="15" viewBox="0 0 16 16" fill="none" stroke="#4cc6e6" stroke-width="1.6"><circle cx="8" cy="8" r="6.5"/><path d="M8 4.5V8l2.5 1.5"/></svg>
      Mon-Sat: 09am to 07:30pm
    </div>
    <div class="item" style="left:323px">
      <svg width="16" height="12" viewBox="0 0 16 12" fill="none" stroke="#4cc6e6" stroke-width="1.5"><rect x="1" y="1" width="14" height="10" rx="1"/><path d="M1 2l7 5 7-5"/></svg>
      needhelp@lorem.com
    </div>
    <div class="links"><span>Faqs</span><span>Pricing</span></div>
    <div class="social"><i></i><i></i><i></i><i></i></div>
  </div>

  <!-- header -->
  <div class="abs header">
    <div class="logo">Halvorsen</div>
    <div class="hinfo" style="left:362px">
      <svg width="36" height="32" viewBox="0 0 36 32" fill="none" stroke="#1f3c6e" stroke-width="2"><path d="M3 10c0-5 30-5 30 0v3h-8V9H11v4H3z"/><rect x="7" y="16" width="22" height="14" rx="3"/><circle cx="18" cy="23" r="3"/></svg>
      <div><b>+12-345-67-8900</b><small>Need help? Make a Call</small></div>
    </div>
    <div class="hinfo" style="left:664px">
      <svg width="32" height="32" viewBox="0 0 32 32" fill="none" stroke="#1f3c6e" stroke-width="2"><circle cx="16" cy="16" r="13"/><path d="M3 16h26M16 3c5 4 5 22 0 26M16 3c-5 4-5 22 0 26"/></svg>
      <div><b>Country</b><small>212A Someplace somewhere</small></div>
    </div>
    <div class="btn-estimate">Free Estimate
      <svg width="20" height="20" viewBox="0 0 20 20" fill="none" stroke="#fff" stroke-width="1.6"><circle cx="10" cy="10" r="8.5"/><path d="M6 10h8M11 7l3 3-3 3"/></svg>
    </div>
  </div>

  <!-- nav -->
  <nav class="abs nav">
    <span class="active">Home</span>
    <span>Clinical Consultation</span>
    <span>Curriculum Vitae &amp; Publications</span>
    <span>Practice Policies</span>
    <span>Contact Us</span>
  </nav>
  <div class="abs nav-phone">
    <svg width="34" height="34" viewBox="0 0 24 24" fill="none" stroke="#6fb8e8" stroke-width="1.4"><path d="M5 3h4l2 5-2.5 1.5a11 11 0 0 0 6 6L16 13l5 2v4a2 2 0 0 1-2 2A16 16 0 0 1 3 5a2 2 0 0 1 2-2z"/></svg>
  </div>

  <!-- hero -->
  <section class="abs hero" role="img" aria-label="Therapist in a session speaking with a client, with a darkened overlay">
    <div class="hero-tag">We are leaders in</div>
    <h1>Psychotherapy</h1>
    <p>Lorem ipsum dolor sit amet, consectetur adipiscing elit, sed do eiusmod tempor i</p>
    <div class="btn-cyan">Read More</div>
  </section>

  <!-- who we are -->
  <div class="ph" role="img" aria-label="Man with glasses taking notes during a counselling session" style="left:89px;top:943px;width:234px;height:418px;background:linear-gradient(160deg,#6b6f74,#2f3338)"></div>
  <div class="ph" role="img" aria-label="Young child sitting on a sofa in a family session" style="left:342px;top:965px;width:234px;height:417px;background:linear-gradient(160deg,#e9e6e2,#9a8f86)"></div>
  <div class="abs" style="left:290px;top:1123px;width:80px;height:80px;border-radius:50%;background:var(--navy);display:flex;align-items:center;justify-content:center">
    <svg width="40" height="40" viewBox="0 0 40 40" fill="none" stroke="#6fb8e8" stroke-width="2"><path d="M8 20a12 12 0 0 1 21-8M32 20a12 12 0 0 1-21 8"/><path d="M29 6v6h-6M11 34v-6h6"/><path d="M20 13c-3 5-4 7-4 9a4 4 0 0 0 8 0c0-2-1-4-4-9z"/></svg>
  </div>
  <div class="abs" style="left:612px;top:952px">
    <div class="eyebrow">Who we are</div>
    <div class="h2" style="margin-top:22px">Your Path to Healing<br>Starts Here</div>
    <div style="font-size:20px;font-weight:500;color:#222;margin-top:22px">Find Balance, Find Harmony</div>
    <p class="body-s" style="width:505px;margin-top:14px">Lorem ipsum dolor sit amet, consectetur adipiscing elit, sed do eiusmod temp or incididunt ut labore et dolore magna aliqua. Ut enim ad minim veniam, quis laboris nisi ut aliquip ex ea commodo consequat.</p>
    <p class="body-s" style="width:505px;margin-top:10px">Lorem ipsum dolor sit amet, consectetur adipiscing elit, sed do eiusmod temp or incididunt ut labore et dolore magna aliqua.</p>
  </div>
  <div class="btn-sq" style="left:610px;top:1322px;width:156px">Contact us
    <svg width="18" height="12" viewBox="0 0 18 12" fill="none" stroke="#fff" stroke-width="1.6"><path d="M1 6h15M11 1l5 5-5 5"/></svg>
  </div>

  <!-- conditions -->
  <section class="abs conditions">
    <div class="eyebrow" style="position:absolute;left:86px;top:62px">Conditons we treat</div>
    <div class="h2" style="position:absolute;left:84px;top:90px;font-size:42px">Conditions We Treat</div>
    <div style="position:absolute;left:942px;top:108px;font-size:15px;color:#222">More Conditions</div>
    <div style="position:absolute;left:1075px;top:98px;width:38px;height:38px;background:var(--navy);display:flex;align-items:center;justify-content:center">
      <svg width="10" height="14" viewBox="0 0 10 14" fill="none" stroke="#fff" stroke-width="2"><path d="M2 1l6 6-6 6"/></svg>
    </div>
    <div class="cond-card" style="left:96px" role="img" aria-label="Child playing with toys during a therapy session">
      <div style="position:absolute;inset:0;background:linear-gradient(180deg,#c9c3bd 0%,#7b8aa3 55%,#2b4a7a 100%)"></div>
      <span class="dot"></span><div class="title">Psychotherapy</div>
      <div class="arrow"><svg width="16" height="12" viewBox="0 0 16 12" fill="none" stroke="#fff" stroke-width="1.5"><path d="M1 6h13M9 1l5 5-5 5"/></svg></div>
    </div>
    <div class="cond-card" style="left:442px" role="img" aria-label="Clasped hands resting on a table">
      <div style="position:absolute;inset:0;background:linear-gradient(180deg,#d8dde3 0%,#8d9db4 55%,#2b4a7a 100%)"></div>
      <span class="dot"></span><div class="title">Clinical Consultation</div>
      <div class="arrow"><svg width="16" height="12" viewBox="0 0 16 12" fill="none" stroke="#fff" stroke-width="1.5"><path d="M1 6h13M9 1l5 5-5 5"/></svg></div>
    </div>
    <div class="cond-card" style="left:788px" role="img" aria-label="Professional with clipboard in a consultation">
      <div style="position:absolute;inset:0;background:linear-gradient(180deg,#e1e1e1 0%,#95a1b5 55%,#2b4a7a 100%)"></div>
      <span class="dot"></span><div class="title">Training &amp; Education</div>
      <div class="arrow"><svg width="16" height="12" viewBox="0 0 16 12" fill="none" stroke="#fff" stroke-width="1.5"><path d="M1 6h13M9 1l5 5-5 5"/></svg></div>
    </div>
  </section>

  <!-- leading expert -->
  <section class="abs expert-band" role="img" aria-label="Faint background photo of a calm pet under a blue overlay">
    <div style="position:absolute;left:90px;top:106px;font-size:40px;font-weight:600;color:#fff;line-height:50px">Leading<br>Expert</div>
    <div class="btn-sq" style="left:91px;top:279px;width:155px;height:46px">Contact us
      <svg width="18" height="12" viewBox="0 0 18 12" fill="none" stroke="#fff" stroke-width="1.6"><path d="M1 6h15M11 1l5 5-5 5"/></svg>
    </div>
  </section>
  <div class="expert-card" style="left:353px">
    <svg style="margin:0 auto" width="38" height="38" viewBox="0 0 38 38" fill="none" stroke="#1aa6c9" stroke-width="2"><circle cx="19" cy="12" r="7"/><path d="M5 35c0-8 6-12 14-12s14 4 14 12z"/></svg>
    <h3>Professionalism</h3>
    <p>Lorem ipsum dolor sit consectetur adipiscing elit, sed do eiusmod tempor incididunt</p>
    <div class="more">Read More <svg width="14" height="10" viewBox="0 0 14 10" fill="none" stroke="#1f3c6e" stroke-width="1.5"><path d="M1 5h11M8 1l4 4-4 4"/></svg></div>
  </div>
  <div class="expert-card" style="left:612px">
    <svg style="margin:0 auto" width="38" height="38" viewBox="0 0 38 38" fill="none" stroke="#1aa6c9" stroke-width="2"><circle cx="19" cy="20" r="15"/><path d="M19 20l7-7M10 20h2M26 20h2M19 11v2"/></svg>
    <h3>Individualized</h3>
    <p>Lorem ipsum dolor sit consectetur adipiscing elit, sed do eiusmod tempor incididunt</p>
    <div class="more">Read More <svg width="14" height="10" viewBox="0 0 14 10" fill="none" stroke="#1f3c6e" stroke-width="1.5"><path d="M1 5h11M8 1l4 4-4 4"/></svg></div>
  </div>
  <div class="expert-card" style="left:873px">
    <svg style="margin:0 auto" width="38" height="38" viewBox="0 0 38 38" fill="none" stroke="#1aa6c9" stroke-width="2"><circle cx="17" cy="9" r="5"/><path d="M12 30c2-8 4-12 10-12M6 35h26M22 18l6 8"/></svg>
    <h3>Confidential</h3>
    <p>Lorem ipsum dolor sit consectetur adipiscing elit, sed do eiusmod tempor incididunt</p>
    <div class="more">Read More <svg width="14" height="10" viewBox="0 0 14 10" fill="none" stroke="#1f3c6e" stroke-width="1.5"><path d="M1 5h11M8 1l4 4-4 4"/></svg></div>
  </div>

  <!-- about the psychologist -->
  <section class="abs aboutme">
    <div class="eyebrow" style="position:absolute;left:0;width:1200px;text-align:center;top:62px">About me</div>
    <div class="h2" style="position:absolute;left:0;width:1200px;text-align:center;top:92px;font-size:42px">About Elias Halvorsen</div>
    <svg style="position:absolute;left:340px;top:230px" width="520" height="320" viewBox="0 0 520 320" fill="none" stroke="#555" stroke-width="1.2">
      <path d="M72 10 A200 200 0 0 0 72 310"/>
      <path d="M448 10 A200 200 0 0 1 448 310"/>
    </svg>
    <div role="img" aria-label="Portrait of the psychologist in a grey blazer" style="position:absolute;left:434px;top:204px;width:326px;height:326px;border-radius:50%;background:radial-gradient(circle at 50% 40%,#8a95b8,#3c4a78 70%)"></div>
    <div class="icircle" style="left:337px;top:262px"><svg width="32" height="32" viewBox="0 0 32 32" fill="none" stroke="#1f3c6e" stroke-width="1.6"><circle cx="16" cy="11" r="4"/><circle cx="7" cy="13" r="3"/><circle cx="25" cy="13" r="3"/><path d="M9 27c0-5 3-8 7-8s7 3 7 8M2 25c0-4 2-6 5-6M30 25c0-4-2-6-5-6"/></svg></div>
    <div class="icircle" style="left:337px;top:437px"><svg width="32" height="32" viewBox="0 0 40 40" fill="none" stroke="#1f3c6e" stroke-width="2"><path d="M8 20a12 12 0 0 1 21-8M32 20a12 12 0 0 1-21 8"/><path d="M20 13c-3 5-4 7-4 9a4 4 0 0 0 8 0c0-2-1-4-4-9z"/></svg></div>
    <div class="icircle" style="left:783px;top:262px"><svg width="32" height="32" viewBox="0 0 38 38" fill="none" stroke="#1f3c6e" stroke-width="2"><circle cx="17" cy="9" r="5"/><path d="M12 30c2-8 4-12 10-12M6 35h26M22 18l6 8"/></svg></div>
    <div class="icircle" style="left:783px;top:437px"><svg width="32" height="32" viewBox="0 0 32 32" fill="none" stroke="#1f3c6e" stroke-width="1.8"><circle cx="16" cy="16" r="5"/><path d="M16 3v4M16 25v4M3 16h4M25 16h4M7 7l3 3M22 22l3 3M25 7l-3 3M10 22l-3 3"/></svg></div>
    <div class="cred" style="position:absolute;left:136px;top:260px"><h4>B.A Psychology</h4><small>New College of Oakridge,<br>1999</small></div>
    <div class="cred" style="position:absolute;left:134px;top:436px"><h4>M.A Clinical<br>Psychology</h4><small>The Westbrook Institute, 2001</small></div>
    <div class="cred" style="position:absolute;left:882px;top:262px"><h4>Psy.D. Clinical<br>Psychology</h4><small>The Westbrook Institute, 2005</small></div>
    <div class="cred" style="position:absolute;left:882px;top:438px"><h4>Advanced Candidate</h4><small>Analytic Training at The Tarn<br>Institute of Bayview</small></div>
  </section>

  <!-- testimonials -->
  <section class="abs testimonials">
    <div class="eyebrow" style="position:absolute;left:0;width:1200px;text-align:center;top:54px;color:var(--cyan-light)">Testimonials</div>
    <div style="position:absolute;left:0;width:1200px;text-align:center;top:84px;font-size:40px;font-weight:600;color:#fff">What Clients are Saying</div>
    <div class="tcard" style="left:92px">
      <svg class="quote" width="34" height="26" viewBox="0 0 34 26" fill="#2fb6dc"><path d="M0 0h14v14l-6 12H2l5-12H0zM19 0h14v14l-6 12h-6l5-12h-7z"/></svg>
      <p>Lorem ipsum dolor sit amet, consectetur adipiscing elit, sed do eiusmod tempor i ncididunt ut labore et dolore magna aliq ua. Ut enim ad minim veniam, quis nostr</p>
      <div class="who"><div class="avatar" role="img" aria-label="Client avatar"></div><div><b>Noah B.</b><small>Australia</small></div></div>
    </div>
    <div class="tcard" style="left:440px">
      <svg class="quote" width="34" height="26" viewBox="0 0 34 26" fill="#2fb6dc"><path d="M0 0h14v14l-6 12H2l5-12H0zM19 0h14v14l-6 12h-6l5-12h-7z"/></svg>
      <p>Lorem ipsum dolor sit amet, consectetur adipiscing elit, sed do eiusmod tempor i ncididunt ut labore et dolore magna aliq ua. Ut enim ad minim veniam, quis nostr</p>
      <div class="who"><div class="avatar" role="img" aria-label="Client avatar"></div><div><b>Noah B.</b><small>Australia</small></div></div>
    </div>
    <div class="tcard" style="left:786px">
      <svg class="quote" width="34" height="26" viewBox="0 0 34 26" fill="#2fb6dc"><path d="M0 0h14v14l-6 12H2l5-12H0zM19 0h14v14l-6 12h-6l5-12h-7z"/></svg>
      <p>Lorem ipsum dolor sit amet, consectetur adipiscing elit, sed do eiusmod tempor i ncididunt ut labore et dolore magna aliq ua. Ut enim ad minim veniam, quis nostr</p>
      <div class="who"><div class="avatar" role="img" aria-label="Client avatar"></div><div><b>Noah B.</b><small>Australia</small></div></div>
    </div>
    <svg style="position:absolute;left:566px;top:454px" width="70" height="10" viewBox="0 0 70 10">
      <circle cx="5" cy="5" r="3" fill="#ccd"/><circle cx="19" cy="5" r="3" fill="#ccd"/>
      <circle cx="35" cy="5" r="4" fill="none" stroke="#e0873a" stroke-width="1.5"/><circle cx="35" cy="5" r="2" fill="#e0873a"/>
      <circle cx="51" cy="5" r="3" fill="#ccd"/><circle cx="65" cy="5" r="3" fill="#ccd"/>
    </svg>
  </section>

  <!-- contact -->
  <div class="abs" style="left:103px;top:3876px;font-size:42px;color:var(--navy)"><b style="font-weight:600">Contact Us</b> Today</div>
  <div class="contact-item" style="top:3958px">
    <svg width="30" height="30" viewBox="0 0 24 24" fill="none" stroke="#1f3c6e" stroke-width="1.2"><path d="M5 3h4l2 5-2.5 1.5a11 11 0 0 0 6 6L16 13l5 2v4a2 2 0 0 1-2 2A16 16 0 0 1 3 5a2 2 0 0 1 2-2z"/></svg>
    <div><b>HEAD OFFICE</b><small>21 Lorem Ipsum, ABC 123</small></div>
  </div>
  <div class="contact-item" style="top:4030px">
    <svg width="32" height="30" viewBox="0 0 32 30" fill="none" stroke="#1f3c6e" stroke-width="1.4"><path d="M2 12l14-10 14 10v16H2z"/><path d="M2 12l14 10 14-10M2 28l11-9M30 28l-11-9"/></svg>
    <div><b>EMAIL ADDRESS</b><small>name@company.com</small></div>
  </div>
  <div class="contact-item" style="top:4096px">
    <svg width="30" height="32" viewBox="0 0 30 32" fill="none" stroke="#1f3c6e" stroke-width="1.4"><path d="M15 30S5 19 5 12a10 10 0 0 1 20 0c0 7-10 18-10 18z"/><circle cx="15" cy="12" r="4"/></svg>
    <div><b>CALL US NOW</b><small>Call Now: 123-456-789</small></div>
  </div>

  <div class="abs form-panel">
    <h3>Send Us A Message</h3>
    <div class="row2">
      <div><label>First Name</label><div class="field">John</div></div>
      <div><label>Last Name</label><div class="field">Doe</div></div>
    </div>
    <div style="margin-top:26px;width:414px"><label>Email</label><div class="field">Info@company.com</div></div>
    <div style="margin-top:28px;width:414px"><label>Message</label><div class="area">Type Your Message</div></div>
    <div class="btn-sq" style="position:relative;margin-top:40px;width:156px;height:46px;background:var(--cyan-light)">Contact us
      <svg width="18" height="12" viewBox="0 0 18 12" fill="none" stroke="#fff" stroke-width="1.6"><path d="M1 6h15M11 1l5 5-5 5"/></svg>
    </div>
  </div>

  <!-- footer -->
  <footer class="abs footer">
    <div class="flogo">Halvorsen</div>
    <div class="finfo" style="left:430px">
      <svg width="32" height="32" viewBox="0 0 32 32" fill="none" stroke="#fff" stroke-width="1.6"><circle cx="16" cy="16" r="13"/><path d="M3 16h26M16 3c5 4 5 22 0 26M16 3c-5 4-5 22 0 26"/></svg>
      <div>123, Building Name, Street<br>City, State XY 123456</div>
    </div>
    <div class="finfo" style="left:688px">
      <svg width="30" height="32" viewBox="0 0 30 32" fill="none" stroke="#fff" stroke-width="1.6"><rect x="3" y="3" width="16" height="26" rx="2"/><path d="M9 25h4M23 10a6 6 0 0 1 0 10M26 7a10 10 0 0 1 0 16"/></svg>
      <div>PHONE<br>(123) 456 7890</div>
    </div>
    <div class="finfo" style="left:864px">
      <svg width="32" height="30" viewBox="0 0 32 30" fill="none" stroke="#fff" stroke-width="1.4"><path d="M2 12l14-10 14 10v16H2z"/><path d="M2 12l14 10 14-10"/></svg>
      <div>EMAIL<br>info@company.com</div>
    </div>
    <div class="fnav"><span>HOME</span><span>SERVICES</span><span>ABOUT US</span><span>TESTIMONIALS</span><span>BLOG</span><span>CONTACT US</span></div>
    <div class="copy">All Rights Reserved. 2023</div>
    <div class="fsocial"><i></i><i></i><i></i><i></i></div>
  </footer>

</div>
</body>
</html>
```